Vehicle Wrapping Company needs a new look

We need to update our website design. We are the largest fleet vehicle wrapping (installation only - we do not print) company in the US. We do not get much business on this site, we use it mainly to update our portfolio/for new clients to see our capabilities. Looking for something modern and clean. We are the innovators in our industry and the best at what we do, our website should represent that. We haven't updated it for a couple years. Our current website: www.varnelwrapworks.com
Industry/Entity Type
Advertising
Coding
Coded - Design and coding required
Number of Pages Required
5+ page
Font styles to use
Other font styles liked:
Look and feel
Each slider illustrates characteristics of the customer's brand and the style your logo design should communicate.

```html
<!DOCTYPE html>
<html lang="en">
<head>
<meta charset="utf-8">
<title>Varnel Wrapworks – Professional Vehicle Wrapping</title>
<link href="https://fonts.googleapis.com/css2?family=Raleway:wght@400;500;600;700&family=Lato:wght@400;700&display=swap" rel="stylesheet">
<style>
:root{
  --orange:#f39a1f;
  --orange-deep:#e8861a;
  --ink:#222222;
  --text:#444444;
  --muted:#777777;
  --panel:#f1f1f1;
  --rule:#e2e2e2;
  --footer:#323232;
  --white:#ffffff;
}
*{margin:0;padding:0;box-sizing:border-box}
html,body{width:1200px;height:2493px;overflow:hidden;background:var(--white)}
body{font-family:'Lato',sans-serif;color:var(--text)}
.page{position:relative;width:1200px;height:2493px;overflow:hidden}
.abs{position:absolute}

/* header */
.site-header{position:absolute;left:0;top:0;width:1200px;height:117px;background:var(--white)}
.brand{position:absolute;left:75px;top:20px;display:flex;align-items:center;gap:10px}
.brand-mark{width:16px;height:76px;background:var(--orange)}
.brand-name{font-family:'Raleway',sans-serif;font-weight:600;font-size:30px;color:var(--ink);letter-spacing:.5px}
.main-nav{position:absolute;top:42px;left:472px;display:flex;gap:0}
.main-nav a{display:block;height:33px;line-height:33px;font-family:'Raleway',sans-serif;font-weight:600;font-size:13px;color:var(--ink);text-decoration:none;letter-spacing:.5px;margin-right:44px}
.main-nav a.active{background:var(--ink);color:var(--white);padding:0 14px;border-left:7px solid var(--orange);margin-right:40px}

/* hero */
.hero{position:absolute;left:0;top:117px;width:1200px;height:548px;background:linear-gradient(90deg,#f0951f 0%,#f5a031 45%,#e9a24a 60%,#8a8580 75%,#6e6e6e 100%)}
.hero-photo{position:absolute;left:430px;top:0;width:770px;height:548px;background:radial-gradient(ellipse at 55% 45%,#f07a20 0%,#e85d1e 22%,#7a3b8a 45%,rgba(90,90,90,.0) 70%)}
.hero-title{position:absolute;left:75px;top:110px;font-family:'Raleway',sans-serif;font-weight:600;font-size:36px;line-height:47px;color:var(--white);letter-spacing:.5px}
.hero-cta{position:absolute;left:75px;top:210px;font-family:'Raleway',sans-serif;font-weight:700;font-size:21px;line-height:28px;color:var(--ink)}
.hero-dots{position:absolute;left:75px;top:308px;display:flex;gap:7px}
.hero-dots span{width:10px;height:10px;border-radius:50%;background:var(--ink)}
.hero-dots span:first-child{background:var(--white)}

/* section heads */
.section-title{position:absolute;left:0;width:1200px;display:flex;justify-content:center;align-items:center;gap:10px;font-family:'Raleway',sans-serif;font-weight:600;font-size:23px;color:var(--ink);letter-spacing:.3px}
.section-title i{display:block;width:10px;height:38px;background:var(--orange)}
.btn{position:absolute;height:38px;line-height:38px;background:var(--ink);color:var(--white);font-family:'Raleway',sans-serif;font-weight:700;font-size:13px;text-align:center;border-left:10px solid var(--orange);letter-spacing:.3px}

/* welcome */
.welcome-bg{position:absolute;left:0;top:665px}
.welcome-text{position:absolute;left:83px;top:772px;width:1034px;text-align:center;font-size:14.5px;line-height:26px;color:var(--text)}

/* services */
.services{position:absolute;left:0;top:1127px;width:1200px;display:grid;grid-template-columns:repeat(4,299px);grid-auto-rows:156px;gap:4px 3px}
.service{position:relative;display:flex;align-items:center;justify-content:center;font-family:'Raleway',sans-serif;font-weight:700;font-size:19px;color:var(--white);letter-spacing:.5px}
.s-buses{background:linear-gradient(135deg,#5a3a7a,#a89ab8)}
.s-retails{background:linear-gradient(135deg,#3f5f8f,#b7c2cf)}
.s-specialty{background:linear-gradient(180deg,#7aa6d6,#8f7f6a)}
.s-tankers{background:linear-gradient(180deg,#6f9a5a,#c23a2a)}
.s-trailers{background:linear-gradient(180deg,#bfc6cc,#6e6e6e)}
.s-trucks{background:linear-gradient(135deg,#1f4f9a,#8e9aa8)}
.s-vans{background:linear-gradient(135deg,#2a5aa8,#9aa7b8)}
.s-cars{background:linear-gradient(135deg,#6a3a9a,#7a8a9a)}

.rule{position:absolute;left:75px;width:1052px;height:1px;background:var(--rule)}

/* portfolio */
.portfolio-sub{position:absolute;left:0;top:1582px;width:1200px;text-align:center;font-size:14px;color:var(--muted)}
.card{position:absolute;top:1642px;width:331px;height:519px;background:var(--panel)}
.card-photo{height:201px}
.p-amp{background:linear-gradient(135deg,#e8401f,#bdbdbd)}
.p-classic{background:linear-gradient(135deg,#e6b23a,#9a1e1e)}
.p-tanker{background:linear-gradient(180deg,#4a7ac8,#c4302a 70%,#555)}
.card h3{margin:24px 20px 0;text-align:center;font-family:'Raleway',sans-serif;font-weight:700;font-size:21px;line-height:28px;color:var(--orange)}
.card p{margin:14px 36px 0;text-align:center;font-size:15px;line-height:26px;color:var(--text)}
.card .btn{left:96px;top:455px;width:140px}
.arrow{position:absolute;top:1883px}

/* partners */
.partner{position:absolute;top:2247px;width:133px;height:64px;border-radius:5px;background:linear-gradient(180deg,#f6f6f6,#c9c9c9);box-shadow:0 2px 3px rgba(0,0,0,.25)}

/* footer */
.site-footer{position:absolute;left:0;top:2353px;width:1200px;height:140px;background:var(--footer)}
.f-brand{position:absolute;left:75px;top:22px;display:flex;align-items:center;gap:8px}
.f-brand .brand-mark{width:8px;height:38px}
.f-brand .brand-name{font-size:20px;color:var(--white)}
.f-copy{position:absolute;left:75px;top:76px;font-size:11px;line-height:20px;color:#9a9a9a}
.f-nav{position:absolute;right:73px;top:28px;display:flex;font-family:'Raleway',sans-serif;font-size:11.5px;font-weight:500}
.f-nav a{color:var(--white);text-decoration:none}
.f-nav span{color:#aaa;margin:0 11px}
.social{position:absolute;right:73px;top:67px;display:flex;gap:6px}
.social span{width:30px;height:30px;border-radius:50%}
</style>
</head>
<body>
<div class="page">

  <header class="site-header">
    <div class="brand"><span class="brand-mark"></span><span class="brand-name">VARNEL WRAPWORKS</span></div>
    <nav class="main-nav">
      <a class="active" href="#">HOME</a>
      <a href="#">ABOUT</a>
      <a href="#">PROJECTS</a>
      <a href="#">PORTFOLIO</a>
      <a href="#">PRESS</a>
      <a href="#">CONTACT</a>
    </nav>
  </header>

  <section class="hero">
    <div class="hero-photo" role="img" aria-label="Photo of a compact car in a bright orange and purple full-body promotional wrap, parked in a lot"></div>
    <h1 class="hero-title">WE ARE A PROFESSIONAL<br>VEHICLE WRAPPING COMPANY</h1>
    <p class="hero-cta">Call us Today for a free.&nbsp; No obligation<br>Quote: 555 014 2290</p>
    <div class="hero-dots"><span></span><span></span><span></span><span></span></div>
  </section>

  <svg class="welcome-bg" width="1200" height="350" viewBox="0 0 1200 350" aria-hidden="true">
    <polygon points="0,0 1200,0 1200,165 600,350 0,165" fill="#f1f1f1"/>
  </svg>
  <h2 class="section-title" style="top:717px"><i></i>WELCOME TO VARNEL WRAPWORKS</h2>
  <p class="welcome-text">Many companies, whether big or small, are adopting outdoor advertisement as a means of reaching their target audiences directly, building their brand and increasing their visibility in the marketplace. Vehicle wraps are being used by companies and car owners to showcase their attention-grabbing designs, campaigns or company logo(s) with the sole purpose of delivering their messages to the masses.</p>
  <div class="btn" style="left:530px;top:884px;width:140px">READ MORE</div>

  <h2 class="section-title" style="top:1050px"><i></i>WHAT WE DO</h2>
  <div class="services">
    <div class="service s-buses" role="img" aria-label="Wrapped purple transit bus">BUSES</div>
    <div class="service s-retails" role="img" aria-label="Wrapped retail kiosk">RETAILS</div>
    <div class="service s-specialty" role="img" aria-label="Wrapped specialty monument sign">SPECIALTY</div>
    <div class="service s-tankers" role="img" aria-label="Wrapped red tanker trucks">TANKERS</div>
    <div class="service s-trailers" role="img" aria-label="Wrapped grocery trailers">TRAILERS</div>
    <div class="service s-trucks" role="img" aria-label="Wrapped blue pickup truck">TRUCKS</div>
    <div class="service s-vans" role="img" aria-label="Wrapped blue service vans">VANS</div>
    <div class="service s-cars" role="img" aria-label="Wrapped purple promotional car">CARS</div>
  </div>

  <div class="rule" style="top:1491px"></div>

  <h2 class="section-title" style="top:1526px"><i></i>OUR PORTFOLIO</h2>
  <p class="portfolio-sub">A Few Of Our Latest Installs</p>

  <svg class="arrow" style="left:44px" width="16" height="24" viewBox="0 0 16 24" aria-hidden="true"><polyline points="13,2 4,12 13,22" fill="none" stroke="#222" stroke-width="4"/></svg>
  <svg class="arrow" style="left:1140px" width="16" height="24" viewBox="0 0 16 24" aria-hidden="true"><polyline points="3,2 12,12 3,22" fill="none" stroke="#222" stroke-width="4"/></svg>

  <article class="card" style="left:75px">
    <div class="card-photo p-amp" role="img" aria-label="Close-up of a guitar amplifier in a red-orange wrap"></div>
    <h3>2014 Musical Instrument<br>Wraps</h3>
    <p>Having the likes of Rowan Hale or Paper Lanterns play an instrument that you wrapped for their performances, and the fact that it will be seen by a large scale of people on television, is both exhilarating and overwhelming"...</p>
    <div class="btn">READ MORE</div>
  </article>
  <article class="card" style="left:435px">
    <div class="card-photo p-classic" role="img" aria-label="Classic car in a glossy red wrap"></div>
    <h3>2014 Musical Instrument<br>Wraps</h3>
    <p>Having the likes of Rowan Hale or Paper Lanterns play an instrument that you wrapped for their performances, and the fact that it will be seen by a large scale of people on television, is both exhilarating and overwhelming"...</p>
    <div class="btn">READ MORE</div>
  </article>
  <article class="card" style="left:796px">
    <div class="card-photo p-tanker" role="img" aria-label="Red tanker truck fleet with wraps"></div>
    <h3>2014 Musical Instrument<br>Wraps</h3>
    <p>Having the likes of Rowan Hale or Paper Lanterns play an instrument that you wrapped for their performances, and the fact that it will be seen by a large scale of people on television, is both exhilarating and overwhelming"...</p>
    <div class="btn">READ MORE</div>
  </article>

  <div class="rule" style="top:2207px"></div>

  <div class="partner" style="left:198px"></div>
  <div class="partner" style="left:367px"></div>
  <div class="partner" style="left:534px"></div>
  <div class="partner" style="left:701px"></div>
  <div class="partner" style="left:868px"></div>

  <footer class="site-footer">
    <div class="f-brand"><span class="brand-mark"></span><span class="brand-name">VARNEL WRAPWORKS</span></div>
    <p class="f-copy">Copyright © 2016. Company Name<br>All Right Reserved</p>
    <nav class="f-nav">
      <a href="#">HOME</a><span>|</span><a href="#">ABOUT</a><span>|</span><a href="#">PROJECTS</a><span>|</span><a href="#">PORTFOLIO</a><span>|</span><a href="#">CONTACT</a>
    </nav>
    <div class="social">
      <span style="background:#3b5a9a"></span>
      <span style="background:#29a9e1"></span>
      <span style="background:#555555"></span>
      <span style="background:#cb2027"></span>
      <span style="background:#dd4b39"></span>
      <span style="background:#e52d27"></span>
    </div>
  </footer>

</div>
</body>
</html>
```